New Website for QWRB Holdings (Property Leasing Company in New Haven)

Design a fully functioning website for a real estate property leasing company. The company has a few properties in New Haven, CT and would like to provide an option for its tenants to pay their rent online. The company should have the ability to generate unique account log in username and password for its tenants so they can make online payments through ACH the website. (The ACH processing part will be coordinated with the bank).

Please take a look at all the pictures I uploaded of New Haven especially the area around Marlow College, you will find that the general style is Gothic and charming.

Also please make use of the pictures of the two properties I have attached to the description.

Please keep Holdings page, Contact Us Page , About Us Page, and please add a page entitled "Tenants".

On the Holdings page I would like to see on the left hand side an interactive map of new haven (Please see a map attached), split by New Haven's neighbourhoods, and showing my properties as pins of sort on the map (I can send you the addresses of the properties upon request). On the same page on the right side I want to see a drop down menu that includes list of New Haven Neighbourhoods. When a neighbourhood is selected you can see in the space underneath the drop-down menu the properties we have in that neighbourhood in large thumbnail format. Also on the map you can see the pins corresponding to those properties change colour. A user can either click on the pin or on the thumbnails to have view more pictures of the property and some details in text.

The tenants page should prompt a login to access- I like your idea of having the company name in two colours, one for QWRB and another for Holdings.Please let me know if you have any questions along the way

-------------------------------------------------------------------------------
Property Descriptions for Holdings Page
The Larch Lodge,

Neighbourhood: Westville
Name: Silas Brennaway House
Building Style: Queen Anne Style
Address: 418 Pellwin Road, New Haven, CT 06515
Number of Units: 3
Unit Names: Unit 1, Unit 2, Unit 3

Property Description

This Westiville home was built in 1897, historically known as The Silas Brennaway House, it is an example of the Queen Anne style. The large carriage house is still intact and sits in the lovely, expansive back garden! An outstanding architectural feature of the house is the turret, giving the home prominence on Pellwin Road. This well maintained home has renovated kitchens in all units, the first floor has granite and red oak cabinetry. New baths and central air in all apartments. All newer mechanicals for each unit, all natural gas. The entire house has replacement windows. The new back deck overlooks the back garden and carriage house. The front steps and porch have also been rebuilt. Roof has 30 year architectural singles and approximately 15 years old, the chimney has just been lined.

Unit 1 Description:

2 Bedrooms, 6 rooms in total.
Amenities: Dishwasher, Central Air, Gas Heating, Porch

Unit 2 Description:

2 Bedrooms, 5 rooms in total.
Amenities: Dishwasher, Central Air, Gas Heating, Balcony

Unit 3 Description:

2 Bedrooms, 4 rooms in total.
Amenities: Dishwasher, Central Air, Gas Heating

The Fern Lodge:

Neighbourhood: East Rock
Name: 64 Birchmere
Building Style: Victorian
Address: 64 Birchmere Lane, New Haven, CT 06511
Number of Units: 2
Unit Names: Unit 1, and Unit 2

Property Description

East Rock incredibly charming newly renovated 2 family on quiet tree-lined block. Tenants are responsible for all utilities (gas heat, electricity and cable). Small pets are possible with landlord approval. Tenants has use of shared yard, laundry in the basement and on street parking only. Located steps away from gourmet markets & minutes to Downtown New Haven, Marlow & local hospitals. Fascinating backyard. This is a feel good house!

Unit 1 Description:

Area:
1100 soft, 3 Bedrooms, 5 rooms in total.
Amenities: In unit Washer and Dryer, Central Air, Gas Heating, Porch, Backyard

Unit 2 Description:

Area: 2,820 sqft
5 Bedrooms, 8 rooms in total.
Amenities: In unit Washer and Dryer, Dishwasher, Central Air, and Gas Heating

Target Market(s)

1-3 bedroom Renting Market around Marlow College and New Haven Community

Industry/Entity Type

Real Estate

Coding

Coded - Design and coding required

Number of Pages Required

4 page

Font styles to use
Other font styles liked:
• Helvetica

Colors
85cae6
cee9f5
d9d9d9
9d9d9d

Requirements
Must have
• Payment page with login (accounts can only be created by administrator)
• A page showcasing the properties (Professional photos to be uploaded shortly)
• A page for technical support, contact information and so forth
• Home page
Nice to have
• A professional, but stylish design. Not too colourful, something with pastel colours
Should not have
• A lot of colours, any pop-ups,

```html
<!DOCTYPE html>
<html lang="en">
<head>
<meta charset="utf-8">
<title>QWRB Holdings — Discover Your Perfect Home</title>
<link rel="stylesheet" href="https://fonts.googleapis.com/css2?family=Open+Sans:wght@400;600;700&family=Oswald:wght@300;400;500&display=swap">
<style>
:root{
  --sky:#85cae6;
  --sky-deep:#5fb3d6;
  --sky-pale:#cee9f5;
  --steel:#2f7fa6;
  --grey-light:#d9d9d9;
  --grey:#9d9d9d;
  --band:#eef1f3;
  --ink:#3a3f44;
  --ink-soft:#6b7177;
  --footer:#262a2e;
  --footer-deep:#1c1f22;
  --white:#ffffff;
}
*{box-sizing:border-box;margin:0;padding:0}
html,body{width:1200px;height:2640px;overflow:hidden}
body{font-family:"Open Sans",Helvetica,Arial,sans-serif;color:var(--ink);background:var(--white);font-size:14px;line-height:1.6}
ul{list-style:none}
.page{position:relative;width:1200px;height:2640px}

/* Header */
.site-header{height:100px;display:flex;align-items:stretch;position:relative;background:var(--white)}
.brand-panel{width:340px;background:var(--sky-pale);display:flex;align-items:center;padding-left:66px;gap:12px}
.brand-mark{width:34px;height:34px;background:var(--sky)}
.brand-name{font-family:"Open Sans",Helvetica,sans-serif;font-weight:700;font-size:24px;color:#1f5d7e;letter-spacing:.5px}
.header-right{flex:1;background:linear-gradient(90deg,var(--sky-pale),var(--white) 30%);position:relative}
.account-links{position:absolute;right:66px;top:12px;font-size:12px;color:var(--ink-soft);display:flex;gap:18px}
.account-links span::before{content:"";display:inline-block;width:8px;height:8px;border-radius:50%;background:var(--grey);margin-right:6px;vertical-align:middle}
.main-nav{position:absolute;right:66px;top:46px;display:flex;gap:8px}
.main-nav a{font-size:13px;font-weight:600;color:var(--ink);text-decoration:none;padding:8px 20px;letter-spacing:.6px;text-transform:uppercase}
.main-nav a.is-active{border:1px solid var(--sky-deep);color:var(--steel)}

/* Hero */
.hero{position:relative;height:460px;overflow:hidden}
.hero-photo{position:absolute;inset:0;background:linear-gradient(180deg,#4a5864 0%,#3a4650 45%,#2f3b31 80%,#26301f 100%)}
.hero-photo::after{content:"";position:absolute;inset:0;background:rgba(10,15,20,.35)}
.hero-copy{position:relative;text-align:center;color:var(--white);padding-top:95px}
.hero-title{font-family:"Oswald",sans-serif;font-weight:500;font-size:70px;line-height:1;letter-spacing:2px;text-transform:uppercase}
.hero-subtitle{font-family:"Oswald",sans-serif;font-weight:300;font-size:40px;letter-spacing:3px;text-transform:uppercase;margin-top:8px}
.hero-text{width:660px;margin:22px auto 0;font-size:13px;line-height:1.7;color:#e8eef2}
.btn-ghost{display:inline-block;margin-top:28px;padding:10px 26px;border:1px solid rgba(255,255,255,.8);color:var(--white);font-size:12px;font-weight:600;letter-spacing:1px;text-transform:uppercase;background:rgba(0,0,0,.25)}
.hero-dots{display:flex;justify-content:center;gap:12px;margin-top:42px}
.hero-dots span{width:10px;height:10px;border-radius:50%;background:rgba(255,255,255,.5)}
.hero-dots span.is-active{background:var(--white)}

/* Features */
.features{background:var(--band);height:260px;padding:40px 66px 0;display:flex;gap:30px}
.feature{flex:1;background:var(--sky-pale);box-shadow:0 6px 10px rgba(0,0,0,.08)}
.feature-head{background:var(--sky);height:92px;display:flex;align-items:center;gap:16px;padding:0 22px}
.feature:nth-child(2) .feature-head{background:var(--sky-deep)}
.feature-icon{width:54px;height:54px;border:2px solid var(--white);border-radius:50%;display:flex;align-items:center;justify-content:center;flex:none}
.feature-title{color:var(--white);font-weight:700;font-size:14px;line-height:1.35;text-transform:uppercase;letter-spacing:.4px}
.feature-body{padding:14px 22px;text-align:center;font-size:12px;color:var(--ink-soft);line-height:1.6}
.btn-small{display:inline-block;margin-top:10px;padding:5px 16px;background:var(--sky-deep);color:var(--white);font-size:11px;font-weight:600;letter-spacing:.6px;text-transform:uppercase}

/* Rentals */
.rentals{background:var(--band);height:740px;padding:30px 0 0;border-top:1px solid var(--grey-light)}
.section-title-row{position:relative;width:1068px;margin:0 auto 30px;text-align:center}
.section-title{font-family:"Oswald",sans-serif;font-weight:400;font-size:26px;color:#555b61;letter-spacing:1.5px;text-transform:uppercase;display:inline-block;padding:0 18px;background:var(--band);position:relative}
.section-title-row::before{content:"";position:absolute;left:0;right:0;top:50%;height:1px;background:var(--grey-light)}
.slider-arrows{position:absolute;right:0;top:4px;display:flex;gap:4px;background:var(--band);padding-left:10px}
.slider-arrows span{width:32px;height:32px;background:var(--grey);display:flex;align-items:center;justify-content:center}
.slider-arrows span:last-child{background:var(--grey-light)}
.rental-list{display:flex;justify-content:center;gap:30px}
.rental-card{width:452px;background:var(--white);box-shadow:0 2px 6px rgba(0,0,0,.08)}
.rental-photo{height:300px}
.rental-photo.is-college{background:linear-gradient(180deg,#8fc3e6 0%,#b7cfd8 40%,#b59a6e 65%,#6f7d4a 100%)}
.rental-photo.is-street{background:linear-gradient(180deg,#6fb0e2 0%,#9ccbe8 35%,#c98b5e 65%,#5e7a3c 100%)}
.rental-stats{height:44px;background:var(--steel);display:flex;justify-content:space-around;align-items:center;color:var(--white);font-size:12px;font-weight:600}
.rental-stats span{display:flex;align-items:center;gap:8px}
.rental-body{padding:18px 26px 26px;text-align:center}
.rental-name{font-weight:700;font-size:16px;text-transform:uppercase;color:var(--ink);letter-spacing:.3px}
.rental-meta{display:flex;justify-content:space-between;align-items:center;margin:12px 0 10px;font-size:12px;color:var(--ink-soft)}
.rental-meta .price{font-weight:700;color:var(--ink)}
.rental-meta .tag{background:var(--sky);color:var(--white);font-size:10px;font-weight:700;padding:2px 10px}
.rental-text{font-size:12px;color:var(--ink-soft);text-align:left;line-height:1.65}
.btn-more{display:inline-block;margin-top:20px;padding:8px 28px;background:var(--sky);color:var(--white);font-size:12px;font-weight:700;letter-spacing:.8px;text-transform:uppercase}

/* Info columns */
.info{height:770px;padding:60px 66px 0;display:flex;gap:50px}
.info-col h3{font-family:"Oswald",sans-serif;font-weight:500;font-size:18px;text-transform:uppercase;letter-spacing:1px;color:var(--ink);margin-bottom:16px}
.why{width:300px}
.why-intro{font-size:12px;color:var(--ink-soft);margin-bottom:22px}
.why-item{display:flex;gap:16px;margin-bottom:26px}
.why-thumb{width:110px;height:84px;flex:none;background:linear-gradient(160deg,#c7b79a,#8f8468 60%,#6e7b58)}
.why-item:nth-child(4) .why-thumb{background:linear-gradient(160deg,#d9d4c8,#a59e8e 60%,#7d7566)}
.why-item:nth-child(5) .why-thumb{background:linear-gradient(160deg,#bcd0dc,#8d9aa3 60%,#6f6e62)}
.why-item p{font-size:12px;color:var(--ink-soft);line-height:1.6}
.testimonials{width:340px}
.quote{background:#f3f4f5;border:1px solid #e6e8ea;padding:24px 24px 24px 64px;position:relative;margin-bottom:30px;font-size:12px;color:var(--ink-soft);line-height:1.7}
.quote::before{content:"\201C";position:absolute;left:20px;top:6px;font-family:Georgia,serif;font-size:56px;color:var(--grey)}
.brokers{flex:1}
.broker-list li{font-size:13px;color:var(--ink-soft);padding:8px 0;border-bottom:1px solid #eef0f2;display:flex;align-items:center;gap:12px}
.broker-list li::before{content:"";width:0;height:0;border-left:6px solid var(--sky-deep);border-top:4px solid transparent;border-bottom:4px solid transparent}

/* Footer */
.site-footer{position:absolute;left:0;right:0;bottom:0;height:310px;background:var(--footer);color:#c5c9cd}
.footer-cols{display:flex;gap:40px;padding:44px 66px 0;height:258px}
.footer-col{flex:1}
.footer-col h4{font-family:"Oswald",sans-serif;font-weight:500;font-size:16px;color:var(--white);letter-spacing:1px;text-transform:uppercase;margin-bottom:16px}
.footer-col li{font-size:12px;line-height:2}
.contact-line{display:flex;align-items:center;gap:10px;font-size:12px;line-height:2.2}
.newsletter p{font-size:12px;margin-bottom:10px}
.field{height:30px;background:#3a3f44;border:1px solid #4a5056;margin-bottom:8px;font-size:11px;color:#8c9298;padding:5px 10px}
.btn-subscribe{display:inline-block;padding:6px 22px;background:var(--sky-deep);color:var(--white);font-size:11px;font-weight:700;letter-spacing:.8px;text-transform:uppercase}
.social li{display:flex;align-items:center;gap:10px}
.social li::before{content:"";width:14px;height:14px;border-radius:50%;background:var(--sky)}
.footer-bottom{height:52px;background:var(--footer-deep);display:flex;align-items:center;padding:0 66px;font-size:11px;color:#8c9298}
</style>
</head>
<body>
<div class="page">

  <header class="site-header">
    <div class="brand-panel">
      <span class="brand-mark"></span>
      <span class="brand-name">QWRB Holdings</span>
    </div>
    <div class="header-right">
      <div class="account-links"><span>Login</span><span>Register</span></div>
      <nav class="main-nav">
        <a class="is-active">Home</a>
        <a>About Us</a>
        <a>Tenants</a>
        <a>Blog</a>
        <a>Contact Us</a>
      </nav>
    </div>
  </header>

  <section class="hero">
    <div class="hero-photo" role="img" aria-label="Historic brick college building with a clock tower behind leafy trees"></div>
    <div class="hero-copy">
      <h1 class="hero-title">Discover Your</h1>
      <p class="hero-subtitle">Perfect Home</p>
      <p class="hero-text">There are many well kept homes waiting for you in New Haven, with charming details and quiet streets close to the college. Whether you need a single room or a family flat, our team will help you find a place that feels right from day one.</p>
      <span class="btn-ghost">Browse More</span>
      <div class="hero-dots"><span class="is-active"></span><span></span><span></span><span></span></div>
    </div>
  </section>

  <section class="features">
    <article class="feature">
      <div class="feature-head">
        <span class="feature-icon"><svg width="24" height="24" viewBox="0 0 24 24" fill="none" stroke="#fff" stroke-width="2"><path d="M12 22s7-7 7-12a7 7 0 0 0-14 0c0 5 7 12 7 12z"/><circle cx="12" cy="10" r="2.5"/></svg></span>
        <span class="feature-title">Find places anywhere<br>in the world</span>
      </div>
      <div class="feature-body">Search our homes by street and area, and see every detail before you book a visit.<br><span class="btn-small">Read More</span></div>
    </article>
    <article class="feature">
      <div class="feature-head">
        <span class="feature-icon"><svg width="24" height="24" viewBox="0 0 24 24" fill="none" stroke="#fff" stroke-width="2"><circle cx="12" cy="8" r="4"/><path d="M4 21c0-4 4-6 8-6s8 2 8 6"/></svg></span>
        <span class="feature-title">We have agents<br>with experience</span>
      </div>
      <div class="feature-body">Our local team knows every block and will guide you through each step of renting.<br><span class="btn-small">Read More</span></div>
    </article>
    <article class="feature">
      <div class="feature-head">
        <span class="feature-icon"><svg width="24" height="24" viewBox="0 0 24 24" fill="none" stroke="#fff" stroke-width="2"><path d="M3 11l9-7 9 7"/><path d="M5 10v10h14V10"/><path d="M10 20v-6h4v6"/></svg></span>
        <span class="feature-title">Buy or rent beautiful<br>properties</span>
      </div>
      <div class="feature-body">Renovated historic houses with modern kitchens, new baths and central air throughout.<br><span class="btn-small">Read More</span></div>
    </article>
  </section>

  <section class="rentals">
    <div class="section-title-row">
      <h2 class="section-title">Our Rental Home</h2>
      <div class="slider-arrows">
        <span><svg width="10" height="12" viewBox="0 0 10 12"><path d="M8 1L2 6l6 5" fill="none" stroke="#fff" stroke-width="2"/></svg></span>
        <span><svg width="10" height="12" viewBox="0 0 10 12"><path d="M2 1l6 5-6 5" fill="none" stroke="#fff" stroke-width="2"/></svg></span>
      </div>
    </div>
    <div class="rental-list">
      <article class="rental-card">
        <div class="rental-photo is-college" role="img" aria-label="Gothic stone college hall with towers under a blue sky"></div>
        <div class="rental-stats">
          <span><svg width="14" height="14" viewBox="0 0 14 14"><rect x="1" y="1" width="12" height="12" fill="none" stroke="#fff" stroke-width="1.5"/></svg>2000 sq ft</span>
          <span><svg width="16" height="12" viewBox="0 0 16 12"><path d="M1 11V2M1 7h14v4M4 7V5h5v2" fill="none" stroke="#fff" stroke-width="1.5"/></svg>3 Bedrooms</span>
          <span><svg width="16" height="12" viewBox="0 0 16 12"><path d="M1 6h14v2a3 3 0 0 1-3 3H4a3 3 0 0 1-3-3z" fill="none" stroke="#fff" stroke-width="1.5"/></svg>4 Bathrooms</span>
        </div>
        <div class="rental-body">
          <h3 class="rental-name">Sweet Home for Small Family</h3>
          <div class="rental-meta"><span>&#9679; Boston, USA</span><span class="price">$ 250,000</span><span class="tag">Rent</span></div>
          <p class="rental-text">A bright family home on a quiet tree lined block, close to shops, parks and the college. Renovated kitchen, new baths, central air and a shared garden out back for warm evenings.</p>
          <span class="btn-more">More</span>
        </div>
      </article>
      <article class="rental-card">
        <div class="rental-photo is-street" role="img" aria-label="Colourful colonial street with palm trees and a domed church"></div>
        <div class="rental-stats">
          <span><svg width="14" height="14" viewBox="0 0 14 14"><rect x="1" y="1" width="12" height="12" fill="none" stroke="#fff" stroke-width="1.5"/></svg>4500 sq ft</span>
          <span><svg width="16" height="12" viewBox="0 0 16 12"><path d="M1 11V2M1 7h14v4M4 7V5h5v2" fill="none" stroke="#fff" stroke-width="1.5"/></svg>5 Bedrooms</span>
          <span><svg width="16" height="12" viewBox="0 0 16 12"><path d="M1 6h14v2a3 3 0 0 1-3 3H4a3 3 0 0 1-3-3z" fill="none" stroke="#fff" stroke-width="1.5"/></svg>4 Bathrooms</span>
        </div>
        <div class="rental-body">
          <h3 class="rental-name">Sweet Home for Small Family</h3>
          <div class="rental-meta"><span>&#9679; Boston, USA</span><span class="price">$ 250,000</span><span class="tag">Rent</span></div>
          <p class="rental-text">A charming two family house with a porch and backyard, steps from markets and minutes to downtown. Laundry in the basement, gas heat and plenty of light in every room.</p>
          <span class="btn-more">More</span>
        </div>
      </article>
    </div>
  </section>

  <section class="info">
    <div class="info-col why">
      <h3>Why Choose Us</h3>
      <p class="why-intro">Local owners who care for every home and answer every tenant quickly.</p>
      <div class="why-item"><div class="why-thumb" role="img" aria-label="Living room interior"></div><p>Well kept homes with renovated kitchens and new baths in every unit.</p></div>
      <div class="why-item"><div class="why-thumb" role="img" aria-label="Bright kitchen interior"></div><p>Pay your rent online with a secure tenant account set up for you.</p></div>
      <div class="why-item"><div class="why-thumb" role="img" aria-label="House exterior on a quiet street"></div><p>Quiet streets close to the college, hospitals and downtown shops.</p></div>
    </div>
    <div class="info-col testimonials">
      <h3>Testimonials</h3>
      <blockquote class="quote">The house was spotless when we moved in and every repair request was handled within a day. We could not have asked for kinder or more helpful landlords in town.</blockquote>
      <blockquote class="quote">Paying rent online saves me time every month. The apartment is warm, quiet and only a short walk from campus, which makes it the perfect place to live.</blockquote>
    </div>
    <div class="info-col brokers">
      <h3>Brokers</h3>
      <ul class="broker-list">
        <li>Always free from repetition</li>
        <li>Always free from repetition</li>
        <li>The standard chunk of Lorem Ipsum</li>
        <li>The standard chunk of Lorem Ipsum</li>
        <li>Investigationes demonstraverunt</li>
        <li>Investigationes demonstraverunt</li>
        <li>The standard chunk of Lorem Ipsum</li>
        <li>Always free from repetition</li>
        <li>Investigationes demonstraverunt</li>
        <li>Always free from repetition</li>
        <li>The standard chunk of Lorem Ipsum</li>
        <li>Investigationes demonstraverunt</li>
      </ul>
    </div>
  </section>

  <footer class="site-footer">
    <div class="footer-cols">
      <div class="footer-col">
        <h4>About Us</h4>
        <ul><li>Home</li><li>About Us</li><li>Tenants</li><li>Blog</li><li>Contact Us</li></ul>
      </div>
      <div class="footer-col">
        <h4>Contact Us</h4>
        <div class="contact-line"><svg width="14" height="12" viewBox="0 0 14 12"><rect x="1" y="1" width="12" height="10" fill="none" stroke="#85cae6" stroke-width="1.4"/><path d="M1 1l6 5 6-5" fill="none" stroke="#85cae6" stroke-width="1.4"/></svg>support@QWRB-Holdings.net</div>
        <div class="contact-line"><svg width="12" height="14" viewBox="0 0 12 14"><rect x="2" y="1" width="8" height="12" rx="1.5" fill="none" stroke="#85cae6" stroke-width="1.4"/></svg>1-555-014-7720</div>
        <div class="contact-line"><svg width="12" height="14" viewBox="0 0 12 14"><rect x="2" y="1" width="8" height="12" rx="1.5" fill="none" stroke="#85cae6" stroke-width="1.4"/></svg>1-555-014-7731</div>
      </div>
      <div class="footer-col newsletter">
        <h4>Newsletter Sign Up</h4>
        <p>Get news of new homes by email.</p>
        <div class="field">Name</div>
        <div class="field">Email</div>
        <span class="btn-subscribe">Subscribe</span>
      </div>
      <div class="footer-col">
        <h4>Social Media Links</h4>
        <ul class="social"><li>Friendline</li><li>Chirper</li><li>Circleplus</li></ul>
      </div>
    </div>
    <div class="footer-bottom">Copyright &copy; 2016 QWRB Holdings. All rights reserved.</div>
  </footer>

</div>
</body>
</html>
```